TalkNest Needs a Brochure Design

We need a brochure (sent as an e-mail message and via mail), to market our professional development seminars. We provide seminars related to autism and non-verbal communication. Brochure should have certain information (see Must Have Priorities) and be designed for target market.

Please submit only 2-3 of your best designs.
Updates

I have added a word file with detail information about the seminar. We want a design that can be sent both as e-mail and regular mail. A 8 x 10 design that can be folded and mailed will meet our requirements. We are hoping that we will be able to send the one page as an e-mail and the back can be used for advertisement.

Target Market(s)

Physicians, Speech-Language Pathologists, Occupational Therapist, Early Intervention Specialists, Special Educators.

Industry/Entity Type

Communication

Font styles to use
Sans Serif

Colors
3176b5
33b7a4
f68d4d

Requirements
Must have
• See the attached file. In addition the brochure must have:
1 Logo for academic accreditation and CEU information.
2. Registration Fees and how to register.
Nice to have
• Photographs.

```html
<!DOCTYPE html>
<html lang="en">
<head>
<meta charset="utf-8">
<title>Mobile Technology to Support Communication in Autism</title>
<link href="https://fonts.googleapis.com/css2?family=Oswald:wght@500;600&family=Roboto+Condensed:wght@400;700&family=Arimo:wght@400;700&display=swap" rel="stylesheet">
<style>
:root{
  --green:#4cb848;
  --green-dark:#3fa33c;
  --blue:#3176b5;
  --banner:#3a86cc;
  --navy:#1f3f8f;
  --red:#c8252c;
  --yellow:#ffe500;
  --teal:#33b7a4;
  --orange:#f68d4d;
  --ink:#111;
  --agenda-time:#14306e;
  --paper:#ffffff;
}
*{margin:0;padding:0;box-sizing:border-box}
html,body{width:928px;height:1200px;overflow:hidden;background:var(--paper)}
.flyer{position:relative;width:928px;height:1200px;overflow:hidden;font-family:"Arimo",Arial,sans-serif;color:var(--ink)}
.hero-photo{position:absolute;left:300px;top:240px;width:628px;height:500px;
  background:radial-gradient(ellipse at 55% 45%,rgba(226,196,170,.5),rgba(200,214,228,.35) 45%,rgba(255,255,255,0) 75%)}
.shapes{position:absolute;left:0;top:0}
.title{position:absolute;left:0;width:928px;top:38px;text-align:center;font-family:"Oswald",sans-serif;font-weight:600;font-size:32px;line-height:1;white-space:nowrap}
.title .t-red{color:var(--red)}.title .t-yellow{color:var(--yellow)}.title .t-navy{color:var(--navy)}
.event{position:absolute;left:80px;top:106px;color:#fff;font-size:26px;line-height:35px;white-space:nowrap}
.event b{font-weight:700}
.section{position:absolute;left:55px;width:820px}
.section h2{font-size:17px;font-weight:700;color:var(--navy);line-height:20px;margin-bottom:3px}
.section.outcomes h2{color:var(--green-dark)}
.section p{font-size:14.4px;line-height:22.5px;text-align:justify}
.section ol{margin:8px 0 0 46px;font-size:14.4px;line-height:22px}
.section ol li{padding-left:8px}
.agenda-title{position:absolute;left:0;width:928px;top:722px;text-align:center;font-family:"Roboto Condensed",sans-serif;font-weight:700;font-size:34px;line-height:40px;color:#fff}
.agenda-col{position:absolute;top:766px;width:270px}
.slot{margin-bottom:26px}
.slot .time{font-weight:700;font-size:17px;color:var(--agenda-time);line-height:21px}
.slot .topic{font-family:"Roboto Condensed",sans-serif;font-size:16px;line-height:20px;color:var(--ink)}
.footer{position:absolute;left:0;top:1086px;width:928px;height:114px;background:var(--paper)}
.badge{position:absolute;left:244px;top:16px;width:172px;height:88px;border:1px solid #bbb}
.badge .seal{position:absolute;left:8px;top:8px;width:50px;height:40px;background:#c9c9c9}
.badge .note{position:absolute;left:64px;top:6px;width:102px;font-size:5.6px;line-height:7px;color:#333}
.badge .note-low{left:8px;top:54px;width:158px}
.brand{position:absolute;left:466px;top:30px;display:flex;align-items:center;gap:10px}
.brand .mark{width:40px;height:40px;background:var(--blue)}
.brand .name{font-size:30px;color:var(--teal);line-height:40px}
.register{position:absolute;left:690px;top:28px;width:220px;font-size:12.5px;line-height:16px;color:var(--ink)}
.register b{color:var(--orange)}
</style>
</head>
<body>
<div class="flyer">
  <div class="hero-photo" role="img" aria-label="Soft photo of an adult hand holding a child's hand"></div>

  <svg class="shapes" width="928" height="1200" viewBox="0 0 928 1200" aria-hidden="true">
    <path d="M0 0H928V92Q640 72 0 86Z" fill="var(--green)"/>
    <path d="M0 86Q500 76 840 80Q880 84 862 130Q830 220 720 236Q500 250 0 246Z" fill="var(--banner)"/>
    <path d="M0 730Q460 696 928 730V1200H0Z" fill="var(--green)"/>
  </svg>

  <h1 class="title"><span class="t-red">MOBILE TECHNOLOGY</span> <span class="t-yellow">TO SUPPORT COMMUNICATION IN</span> <span class="t-navy">AUTISM</span></h1>

  <div class="event">
    Speaker: <b>Marcus Delane, Ph.D., CCC-SLP</b><br>
    Date: <b>September 20, 2014</b><br>
    Location: <b>240 W Harbor Street, Brookfield, Il 60513</b>
  </div>

  <section class="section instructor" style="top:252px">
    <h2>Instructor:</h2>
    <p>Marcus Delane is an Associate Professor of Communication Disorders at Lakeshore Valley University. He earned his doctorate from Halden University. He has working experience in diverse settings including private practice, hospitals, long-term residential settings and integrated school-settings. His areas of research interest are: assistive technology, early language intervention, and reading disabilities. He has over 30 publications and over 100 presentations at national and international scientific meetings. He is a consulting editor for Journal of Assisted Expression.</p>
  </section>

  <section class="section course" style="top:408px">
    <h2>Course Description:</h2>
    <p>With the current availability of mobile technology (e.g., Orchard Slate, Nimbus OS) individuals with autism have many options available for communication. This course focused on visual support, accessibility, and language learning through mobile technology. Compared specialized AAC “apps” and assessed contemporary evidence for effective use of mobile technology by children with autism to enhance their communication skills.</p>
  </section>

  <section class="section outcomes" style="top:548px">
    <h2>Learner’s Outcomes:</h2>
    <p>As a result of this seminar, the participant will be able to:</p>
    <ol>
      <li>summarize issues related to information processing, visual attention, and visual support in children with autism.</li>
      <li>decide about accessibility of mobile technology by children with autism.</li>
      <li>integrate language learning strategies using mobile technology for children with autism.</li>
      <li>compare contemporary specialized AAC “apps” for children with autism.</li>
      <li>assess contemporary evidence for effectiveness of mobile technology by children with autism.</li>
    </ol>
  </section>

  <h2 class="agenda-title">Time-Ordered Agenda:</h2>

  <div class="agenda-col" style="left:55px">
    <div class="slot"><div class="time">8:30 a.m. – 9:00 a.m.</div><div class="topic">Registration and Coffee</div></div>
    <div class="slot"><div class="time">9:00 a.m. – 10:00 a.m.</div><div class="topic">Information Processing,<br>visual attention, and visual<br>support in children with autism</div></div>
    <div class="slot"><div class="time">10:00 a.m. – 10:45 a.m.</div><div class="topic">Accessibility issues related to<br>use of mobile technology</div></div>
    <div class="slot"><div class="time">10:45 a.m. – 11:00 a.m.</div><div class="topic">Break</div></div>
  </div>

  <div class="agenda-col" style="left:334px;top:792px">
    <div class="slot"><div class="time">11:00 a.m. – 12:00 noon</div><div class="topic">Language learning strategies<br>using mobile technology</div></div>
    <div class="slot"><div class="time">12:00 noon – 12:30 p.m.</div><div class="topic">Lunch</div></div>
    <div class="slot"><div class="time">12:30 p.m. – 1:00 p.m.</div><div class="topic">Video presentations</div></div>
    <div class="slot"><div class="time">1:00 p.m. – 1:45 p.m.</div><div class="topic">Contemporary specialized AAC<br>apps for children with autism</div></div>
  </div>

  <div class="agenda-col" style="left:613px;top:792px">
    <div class="slot"><div class="time">1:45 p.m. – 2:00 p.m.</div><div class="topic">Break</div></div>
    <div class="slot"><div class="time">2:00 p.m. – 2:30 p.m.</div><div class="topic">Assessment of contemporary<br>evidence for effectiveness of mobile<br>technology</div></div>
    <div class="slot"><div class="time">2:30 p.m. – 3:00 p.m.</div><div class="topic">Wrap up discussion, questions, and<br>comments</div></div>
  </div>

  <footer class="footer">
    <div class="badge">
      <div class="seal"></div>
      <p class="note"><b>Lakeshore Valley University</b> is approved by the National Continuing Education Board to provide continuing education activities in speech-language pathology.</p>
      <p class="note note-low">See course information for number of CEUs, level and content area. Approval does not imply endorsement of course content or clinical procedures.</p>
    </div>
    <div class="brand"><span class="mark"></span><span class="name">TalkNest</span></div>
    <p class="register"><b>Registration fee: $150</b><br>Register online at talknest.org/seminars or call (555) 014-2290</p>
  </footer>
</div>
</body>
</html>
```